Package design for small honey and vegetable farm

I would like to have a unique design for the packaging of our honey and vegetables. I have attached the logo from our farm "Willowbrook Acres" that should be on the packaging for both the honey and the vegetables

For the honey the writing, "100% pure organic honey" must be on the packaging in some place. As well as "from the busy bees at Willowbrook Acres". I have attached some designs that I like.

For the vegetables. The design will need to go on a box like the one in the attached image. The phrase "Organically Grown" should be on the package. I would like the background color of the package to be black. I think I would also like to see some stylized vegetables (tomatoes in particular) on the package.

I would like to be able to get all the colors (RGB) used in the designs so I can pass them on to printers.

Industry/Entity Type

Farm

Colors
fbee3e

Requirements
Must have
• For the honey, the package it must say "100% pure organic honey".
• For the vegetables I would like the background color to be black. I would also like some stylized vegetables (tomatoes in particular) added to the package.

```html
<!DOCTYPE html>
<html lang="en">
<head>
<meta charset="utf-8">
<title>Willowbrook Acres Packaging</title>
<link href="https://fonts.googleapis.com/css2?family=Oswald:wght@400;500&display=swap" rel="stylesheet">
<style>
  :root {
    --honey-gold: #fbee3e;
    --honey-deep: #e3a62a;
    --honey-mid: #f5c61f;
    --ink: #000000;
    --paper: #ffffff;
    --tomato-light: #e0506a;
    --tomato-deep: #a8193a;
  }
  * { margin: 0; padding: 0; box-sizing: border-box; }
  html, body { width: 1200px; height: 647px; overflow: hidden; background: var(--paper); }
  .canvas { position: relative; width: 1200px; height: 647px; font-family: "Oswald", sans-serif; }
  .shapes { position: absolute; inset: 0; width: 1200px; height: 647px; }
  .text { position: absolute; left: 0; width: 100%; text-align: center; white-space: nowrap; line-height: 1.2; }
  .brand-name { font-weight: 500; letter-spacing: 1px; }
  .honey-brand { top: 64px; left: 444px; width: 292px; font-size: 20px; color: var(--ink); }
  .honey-title { top: 131px; left: 446px; width: 288px; font-size: 21px; color: var(--paper); font-weight: 400; }
  .honey-sub { top: 164px; left: 446px; width: 288px; font-size: 9.5px; color: var(--ink); text-transform: uppercase; }
  .honey-qualities { top: 218px; left: 446px; width: 288px; font-size: 12px; color: var(--ink); word-spacing: 2px; }
  .honey-qualities .dot { display: inline-block; width: 5px; height: 5px; border-radius: 50%; background: var(--ink); margin: 0 8px 2px; vertical-align: middle; }
  .honey-weight { top: 207px; left: 697px; width: auto; font-size: 9.5px; color: var(--ink); text-align: left; }
  .veg-brand { top: 370px; font-size: 28px; color: var(--paper); }
  .veg-title { top: 462px; font-size: 54px; font-weight: 500; color: var(--paper); letter-spacing: 0.5px; }
</style>
</head>
<body>
<main class="canvas">
  <svg class="shapes" viewBox="0 0 1500 809">
    <defs>
      <linearGradient id="gold-band" x1="0" x2="1" y1="0" y2="0">
        <stop offset="0" stop-color="#e3a62a"/>
        <stop offset="0.5" stop-color="#fbee3e"/>
        <stop offset="1" stop-color="#e3a62a"/>
      </linearGradient>
      <linearGradient id="comb-fill" x1="0" x2="1" y1="0" y2="0">
        <stop offset="0" stop-color="#f5c61f"/>
        <stop offset="0.5" stop-color="#fbee3e"/>
        <stop offset="1" stop-color="#f5c61f"/>
      </linearGradient>
      <radialGradient id="tomato-fill" cx="0.4" cy="0.4" r="0.7">
        <stop offset="0" stop-color="#e0506a"/>
        <stop offset="1" stop-color="#a8193a"/>
      </radialGradient>
    </defs>

    <rect class="honey-band" x="437" y="72" width="602" height="210" fill="url(#gold-band)"/>
    <path class="honeycomb" d="M620 45 L680 10 L740 45 L800 10 L860 45 L860 115 L920 150 L920 215 L860 250 L860 320 L800 352 L740 320 L680 352 L620 320 L620 250 L555 215 L555 150 L620 115 Z"
          fill="url(#comb-fill)" stroke="#000" stroke-width="3"/>
    <rect class="honey-title-bar" x="557" y="158" width="361" height="47" fill="#000"/>

    <rect class="veg-band" x="0" y="397" width="1500" height="412" fill="#000"/>
    <path class="veg-frame" d="M590 443 H68 V762 H1432 V443 H905" fill="none" stroke="#fff" stroke-width="6"/>
    <rect class="tomato-art" x="40" y="455" width="330" height="285" rx="40" fill="url(#tomato-fill)"
          role="img" aria-label="Watercolour illustration of four ripe tomatoes"/>
    <rect class="tomato-art" x="1165" y="465" width="305" height="275" rx="40" fill="url(#tomato-fill)"
          role="img" aria-label="Watercolour illustration of four ripe tomatoes"/>
  </svg>

  <div class="text brand-name honey-brand">Willowbrook Acres</div>
  <div class="text honey-title">100% PURE ORGANIC HONEY</div>
  <div class="text honey-sub">from the busy bees at Willowbrook Acres</div>
  <div class="text honey-qualities">NATURAL<span class="dot"></span>HEALTHY<span class="dot"></span>DELICIOUS</div>
  <div class="text honey-weight">NET WT 12OZ (340G)</div>

  <div class="text brand-name veg-brand">Willowbrook Acres</div>
  <div class="text veg-title">ORGANICALLY GROWN</div>
</main>
</body>
</html>
```